Two Web Pages Design for an Anti-Aging Med Spa

Hi,
We are looking to redesign our website which is an Medspa in the Anti-Aging and Hormone Replacement business. We only need two pages designed. Frontpage and one inner page. and we need professional clean looks with matching colors to our logo (see attached files).
Sites we like:
http://velmorabeauty.example/
http://www.brindlecove.example/

Target Market(s)

Mid-Age Men and Women

Industry/Entity Type

Business

Number of Pages Required

2 page

Font styles to use
Sans Serif

Colors
86cfc6
33b7a4
33a6d7
85cae6
ffffff
cadf82
9bcb3b
fde08a

Requirements
Must have
• IMPORTANT: YOU WOULD ONLY NEED TO DESIGN THE FRONTPAGE AND ONE INNER PAGE, NOT THE WHOLE SITE. FRONT-PAGE MUST INCLUDE A SLIDER. If you have any other questions please PM me.

```html
<!DOCTYPE html>
<html lang="en">
<head>
<meta charset="utf-8">
<title>Evermore Vital – Anti-Aging Med Spa</title>
<link rel="stylesheet" href="https://fonts.googleapis.com/css2?family=Open+Sans:wght@400;600;700&family=Bebas+Neue&family=Lobster+Two:ital,wght@1,700&display=swap">
<style>
:root{
  --teal:#33b7a4;
  --teal-soft:#86cfc6;
  --blue:#33a6d7;
  --blue-soft:#85cae6;
  --green:#9bcb3b;
  --green-soft:#cadf82;
  --white:#ffffff;
  --ink:#333333;
  --text:#555555;
  --page:#f1f1f1;
  --footer-dark:#1f9a88;
}
*{box-sizing:border-box;margin:0;padding:0}
html,body{width:704px;height:1200px;overflow:hidden}
body{font-family:"Open Sans",Arial,sans-serif;background:var(--page);position:relative;color:var(--text)}
.abs{position:absolute}

/* header */
.site-header{position:absolute;left:0;top:0;width:704px;height:63px;background:#f4f4f4}
.brand{left:98px;top:12px;display:flex;align-items:center;gap:6px}
.brand-mark{width:22px;height:22px;border-radius:50%;background:var(--green)}
.brand-name{font-weight:700;font-size:15px;color:var(--ink);letter-spacing:.5px}
.social{right:99px;top:6px;display:flex;gap:5px}
.social span{width:15px;height:15px;border-radius:50%;border:1px solid var(--teal)}
.contact-line{right:99px;top:42px;font-size:8.5px;font-weight:700;color:var(--ink);display:flex;align-items:center;gap:4px}
.contact-line .call{color:var(--green)}
.contact-line .or{background:var(--green);color:#fff;border-radius:50%;width:16px;height:16px;display:flex;align-items:center;justify-content:center;font-size:7px}

.main-nav{position:absolute;left:0;top:63px;width:704px;height:20px;background:var(--teal)}
.main-nav ul{list-style:none;display:flex;position:absolute;left:98px;top:0;height:20px;align-items:center}
.main-nav li{font-size:7.5px;color:#fff;padding:0 8px;height:20px;line-height:20px}
.main-nav li.home{padding:0 6px 0 4px}
.main-nav li.active{background:var(--green)}
.submenu{left:167px;top:89px;width:100px;background:var(--green);opacity:.92;font-size:7px;color:#fff}
.submenu div{padding:5px 9px;border-bottom:1px solid rgba(255,255,255,.4)}

/* hero slider */
.hero{left:0;top:83px;width:704px;height:220px;background:linear-gradient(180deg,#bfe0f2 0%,#e6f2f6 35%,#5cd0d4 48%,#2bbfc6 70%,#cfe8df 100%)}
.hero-figure{left:370px;top:0;width:210px;height:220px;background:linear-gradient(180deg,#d9b59a,#c59479)}
.hero-title{left:157px;top:60px;font-family:"Lobster Two",cursive;font-style:italic;font-weight:700;color:#fff;font-size:19px;line-height:23px;text-shadow:0 1px 2px rgba(0,0,0,.25)}
.dots{left:331px;top:287px;display:flex;gap:2px}
.dots span{width:8px;height:8px;background:#fff}
.dots span:first-child{background:#8a2c2c}

/* form bands */
.band{left:0;width:704px;height:49px}
.band-news{top:304px;background:var(--green)}
.band-register{top:727px;background:var(--blue)}
.band-label{left:0;top:0;height:49px;width:280px;background:var(--teal);clip-path:polygon(0 0,262px 0,280px 24.5px,262px 49px,0 49px)}
.band-label::after{content:"";position:absolute}
.band-title{left:104px;top:5px;font-family:"Bebas Neue",sans-serif;color:#fff;font-size:20px;line-height:19px}
.band-note{left:104px;top:25px;width:160px;font-size:5.4px;font-style:italic;color:#fff;line-height:7.5px}
.field{top:13px;height:23px;font-size:6.5px;font-style:italic;color:#666;padding:0 6px;line-height:23px;display:flex;justify-content:space-between}
.band-news .field{background:var(--green-soft)}
.band-register .field{background:var(--blue-soft)}
.field-name{left:290px;width:103px}
.field-email{left:396px;width:102px}
.send{left:503px;top:13px;width:102px;height:23px;background:var(--teal);border:1px solid #21907f;color:#fff;font-size:8px;font-weight:700;text-align:center;line-height:21px}

/* services */
.service{top:372px;width:124px;height:170px;background:var(--green);border-radius:2px;overflow:hidden}
.service-photo{height:79px}
.diamond{left:50%;width:26px;height:26px;background:#fff;transform:translateX(-50%) rotate(45deg)}
.service h3{font-weight:400;color:#fff;font-size:11px;padding:16px 4px 0;line-height:12px}
.service p{font-size:6.2px;color:#fff;line-height:8.5px;padding:3px 6px 0}
.more{left:33px;top:152px;width:57px;height:14px;background:var(--blue);color:#fff;font-size:6.5px;text-align:center;line-height:14px}

/* welcome */
.welcome-title{left:104px;top:589px;font-size:18px;color:var(--teal);font-weight:400}
.welcome-text{left:104px;top:618px;width:293px;font-size:6.4px;line-height:9.3px;color:#555}
.welcome-photo{left:426px;top:595px;width:169px;height:104px;border:1px solid var(--teal);padding:2px;background:#fff}
.welcome-photo div{width:100%;height:100%;background:linear-gradient(180deg,#d8dde2,#9aa0a6)}

/* testimonials */
.section-title{left:0;width:704px;top:795px;text-align:center;font-family:"Lobster Two",cursive;font-style:italic;font-weight:700;font-size:17px;color:var(--green)}
.title-rule{left:219px;top:820px;width:266px;height:2px;background:var(--green)}
.arrow{top:900px}
.quote{top:844px;width:144px;height:172px;background:var(--green);border-radius:2px;overflow:hidden}
.quote-photo{height:79px}
.quote p{font-size:6.3px;color:#fff;line-height:8.7px;padding:20px 10px 0}
.quote h4{left:10px;top:155px;font-size:8.5px;color:#fff;letter-spacing:.8px}

/* footer */
.site-footer{left:0;top:1033px;width:704px;height:151px;background:var(--teal)}
.footer-heading{font-size:12.5px;color:#111;top:12px}
.footer-links{left:98px;top:33px;list-style:none;font-size:7px;line-height:12.4px;color:var(--green-soft)}
.footer-map{left:257px;top:29px;width:167px;height:109px;background:linear-gradient(135deg,#e9e6dc,#d6e3cf)}
.footer-contact{left:502px;top:33px;font-size:7px;line-height:12.4px;color:var(--green-soft)}
.copyright{left:0;top:1184px;width:704px;height:16px;background:var(--footer-dark);font-size:6px;color:#111;text-align:center;line-height:16px}
</style>
</head>
<body>

<header class="site-header">
  <div class="abs brand"><span class="brand-mark"></span><span class="brand-name">EVERMORE VITAL</span></div>
  <div class="abs social"><span></span><span></span><span></span><span></span></div>
  <div class="abs contact-line">
    <span class="call">CALL</span>
    <svg width="9" height="9" viewBox="0 0 10 10"><path d="M2 1l2 2-1 1.5a6 6 0 0 0 2.5 2.5L7 6l2 2-1.5 1.5C4.5 9 1 5.5.5 2.5z" fill="#333"/></svg>
    <span>555-014-2270</span><span class="or">OR</span>
    <svg width="9" height="7" viewBox="0 0 10 8"><rect x=".5" y=".5" width="9" height="7" fill="none" stroke="#333"/><path d="M.5.5L5 4.5 9.5.5" fill="none" stroke="#333"/></svg>
    <span>hello@evermorevital.example</span>
  </div>
</header>

<nav class="main-nav">
  <ul>
    <li class="home"><svg width="12" height="10" viewBox="0 0 12 10"><path d="M6 0L0 5h2v5h3V7h2v3h3V5h2z" fill="#fff"/></svg></li>
    <li>About Us</li>
    <li class="active">Hormone Replacement</li>
    <li>Rejuvenation</li>
    <li>Weight and Health</li>
    <li>Blog</li>
    <li>Shop</li>
    <li>Testimonials</li>
    <li>Contact Us</li>
  </ul>
</nav>

<section class="abs hero" role="img" aria-label="Slider photo: smiling woman resting her chin on her hand beside a turquoise beach">
  <div class="abs hero-figure" role="img" aria-label="Woman portrait area"></div>
  <h1 class="abs hero-title">Lorem Ipsum. Proin gravida<br>nibh vel velit auctor aliquet.<br>Aenean sollicitudin.</h1>
  <div class="abs dots"><span></span><span></span><span></span><span></span></div>
</section>
<div class="abs submenu"><div>BHRT for Women</div><div>BHRT for Men</div></div>

<section class="abs band band-news">
  <div class="abs band-label"></div>
  <h2 class="abs band-title">Newsletter Signup</h2>
  <p class="abs band-note">Sign up for our monthly newsletter and stay informed on new services and specials. There will be some freebies along the way, too. We do not spam! Ever.</p>
  <div class="abs field field-name">Name..<span>&#9679;</span></div>
  <div class="abs field field-email">Email..<span>&#9993;</span></div>
  <div class="abs send">SEND</div>
</section>

<section class="services">
  <article class="abs service" style="left:98px">
    <div class="service-photo" role="img" aria-label="Woman touching her smooth skin" style="background:linear-gradient(180deg,#e6e6e6,#d4b29a)"></div>
    <div class="abs diamond" style="top:66px"></div>
    <h3>DERMAFILL treatment</h3>
    <p>Lorem Ipsum. Proin gravida nib vel velit auctor aliquet. Aenean sol licit udin, lorem quis bibend um auctor..</p>
    <div class="abs more">Learn more</div>
  </article>
  <article class="abs service" style="left:226px">
    <div class="service-photo" role="img" aria-label="Runner's legs on a track" style="background:linear-gradient(180deg,#4a4a4a,#8a8580)"></div>
    <div class="abs diamond" style="top:66px"></div>
    <h3>Orthopedic Uses</h3>
    <p>Lorem Ipsum. Proin gravida nib vel velit auctor aliquet. Aenean sol licit udin, lorem quis bibend um auctor..</p>
    <div class="abs more">Learn more</div>
  </article>
  <article class="abs service" style="left:354px">
    <div class="service-photo" role="img" aria-label="Couple playing outdoors under a blue sky" style="background:linear-gradient(180deg,#3f7fd0,#a9c8ee)"></div>
    <div class="abs diamond" style="top:66px"></div>
    <h3>Vitamin Bar</h3>
    <p>Lorem Ipsum. Proin gravida nib vel velit auctor aliquet. Aenean sol licit udin, lorem quis bibend um auctor..</p>
    <div class="abs more">Learn more</div>
  </article>
  <article class="abs service" style="left:482px">
    <div class="service-photo" role="img" aria-label="Clinic consultation with a patient" style="background:linear-gradient(180deg,#e2e2e2,#9c9c9c)"></div>
    <div class="abs diamond" style="top:66px"></div>
    <h3>hCG Diet Plan</h3>
    <p>Lorem Ipsum. Proin gravida nib vel velit auctor aliquet. Aenean sol licit udin, lorem quis bibend um auctor..</p>
    <div class="abs more">Learn more</div>
  </article>
</section>

<section class="welcome">
  <h2 class="abs welcome-title">Welcomet to Evermore Vital</h2>
  <p class="abs welcome-text">Lorem Ipsum. Proin gravida nibh vel velit auctor aliquet. Aenean sollicitudin, lorem quis bibendum auctor, nisi elit consequat ipsum, nec sagittis sem nibh id elit. Duis sed odio sit amet nibh vulputate cursus a sit amet mauris. Morbi accumsan ipsum velit. Nam nec tellus a odio tincidunt auctor a ornare odio. Sed non&nbsp; mauris vitae erat consequat auctor eu in elit. Class aptent taciti sociosqu ad litora torquent per conubia nostra, per inceptos himenaeos. Mauris in erat justo. Nullam ac urna eu fel dapibus condimentum sit amet a augue. Sed non neque elit. Sed ut imperdiet nisi. Proin condimentum fermentum nunc. Etiam pharetra, erat sed fermentum feugiat.</p>
  <div class="abs welcome-photo"><div role="img" aria-label="Staff at the clinic front desk"></div></div>
</section>

<section class="abs band band-register">
  <div class="abs band-label"></div>
  <h2 class="abs band-title" style="top:9px;font-size:16.5px;line-height:17px">Register Today for our<br>Upcoming Summer Offers</h2>
  <div class="abs field field-name">Name..<span>&#9679;</span></div>
  <div class="abs field field-email">Email..<span>&#9993;</span></div>
  <div class="abs send">SUBMIT</div>
</section>

<section class="testimonials">
  <h2 class="abs section-title">What saying&nbsp; Our Happy Customer</h2>
  <div class="abs title-rule"></div>
  <svg class="abs arrow" style="left:104px" width="14" height="44" viewBox="0 0 14 44"><path d="M13 1L1 22l12 21" fill="none" stroke="#bbb"/></svg>
  <svg class="abs arrow" style="left:586px" width="14" height="44" viewBox="0 0 14 44"><path d="M1 1l12 21L1 43" fill="none" stroke="#bbb"/></svg>
  <article class="abs quote" style="left:130px">
    <div class="quote-photo" role="img" aria-label="Portrait of a happy customer" style="background:linear-gradient(180deg,#e4e8ea,#b9c2c8)"></div>
    <div class="abs diamond" style="top:66px"></div>
    <p>Lorem Ipsum. Proin gravida nib vel velit auctor aliquet. Aenean sol licit udin, lorem quis bibend Lorem Ipsum. Proin gravida nib vel velit auctor aliquet. Aenean sol licit udin, lorem quisvel velit auctor aliquet gravida nib vel</p>
    <h4 class="abs">NADIA R.</h4>
  </article>
  <article class="abs quote" style="left:281px">
    <div class="quote-photo" role="img" aria-label="Portrait of a happy customer" style="background:linear-gradient(180deg,#b33a3a,#6f8a4a)"></div>
    <div class="abs diamond" style="top:66px"></div>
    <p>Lorem Ipsum. Proin gravida nib vel velit auctor aliquet. Aenean sol licit udin, lorem quis bibend Lorem Ipsum. Proin gravida nib vel velit auctor aliquet. Aenean sol licit udin, lorem quisvel velit auctor aliquet</p>
    <h4 class="abs">HELEN K.</h4>
  </article>
  <article class="abs quote" style="left:431px">
    <div class="quote-photo" role="img" aria-label="Portrait of a happy customer" style="background:linear-gradient(180deg,#dfe6ea,#9eb1bb)"></div>
    <div class="abs diamond" style="top:66px"></div>
    <p>Lorem Ipsum. Proin gravida nib vel velit auctor aliquet. Aenean sol licit udin, lorem quis bibend um auctor gravida nib Lorem Ipsum. Proin gravida nib vel velit auctor aliquet. Aenean sol licit udin, lorem quisvel</p>
    <h4 class="abs">LAURA P.</h4>
  </article>
</section>

<footer class="abs site-footer">
  <h3 class="abs footer-heading" style="left:98px;font-weight:400">BROWS SITE</h3>
  <ul class="abs footer-links">
    <li>Home</li><li>About Us</li><li>Hormone Replacement</li><li>Rejuvenation</li><li>Weight and Health</li><li>Blog</li><li>Shop</li><li>Testimonials</li><li>Contact Us</li>
  </ul>
  <h3 class="abs footer-heading" style="left:256px;font-weight:400">OUR LOCATION</h3>
  <div class="abs footer-map" role="img" aria-label="Street map showing the clinic location"></div>
  <h3 class="abs footer-heading" style="left:502px;font-weight:400">CONTACT INFO</h3>
  <div class="abs footer-contact">
    <div style="padding-left:11px">1207 Harbor Lane<br>Suite 4<br>Coral Point, Florida 30012</div>
    <div style="padding-left:11px;margin-top:10px">555-014-2270<br>555-014-2271<br>hello@evermorevital.example</div>
  </div>
  <svg class="abs" style="left:502px;top:36px" width="7" height="9" viewBox="0 0 7 9"><path d="M3.5 0A3 3 0 0 0 .5 3c0 2 3 6 3 6s3-4 3-6a3 3 0 0 0-3-3z" fill="#cadf82"/><circle cx="3.5" cy="3" r="1" fill="#33b7a4"/></svg>
  <svg class="abs" style="left:502px;top:108px" width="7" height="7" viewBox="0 0 10 10"><path d="M2 1l2 2-1 1.5a6 6 0 0 0 2.5 2.5L7 6l2 2-1.5 1.5C4.5 9 1 5.5.5 2.5z" fill="#cadf82"/></svg>
  <svg class="abs" style="left:502px;top:121px" width="7" height="7" viewBox="0 0 10 10"><path d="M2 1l2 2-1 1.5a6 6 0 0 0 2.5 2.5L7 6l2 2-1.5 1.5C4.5 9 1 5.5.5 2.5z" fill="#cadf82"/></svg>
  <svg class="abs" style="left:502px;top:133px" width="8" height="6" viewBox="0 0 10 8"><rect x=".5" y=".5" width="9" height="7" fill="none" stroke="#cadf82"/><path d="M.5.5L5 4.5 9.5.5" fill="none" stroke="#cadf82"/></svg>
</footer>
<div class="abs copyright">Copyright © 2014&nbsp; Evermore Vital Institute Age Care Studio. All rights reserved.</div>

</body>
</html>
```